Business Card Design for Translation Company - Rush

Rush job for a business card designing for a company doing international translations, several Asian and western languages. Already have a logo design (see attached) to use as the basis of the business card design. For the card, we also need the full company name, address, email, and phone number. In addition, my name as I will be the one handing out the cards.

For the logo design, we think the white background would be best. But we will consider using the dark background if you have a great idea for it.

The attached jpeg design has just been approved, but the designer has not yet finalized the file. When we select our final applicant, we will send the finalized file. (Nothing changes except the quality of the data.)

The phone number may change and if so, we will send the new one when we select our applicant.

We must complete the entire process and have a design ready to go to print no later than 01:00 am August 3, New York (East Coast) time.

We look forward to your participation in the project,
Gus

Target Market(s)

Translation clients worldwide.

Industry/Entity Type

Business

Contact Information for Business Card

Company details:

Korvani Languages Worldwide, Ltd.

#527-2368 Halden Crescent, Victoria, BC, Canada V9T3K2

gdresner@korvanilanguages.example

+1-888-604-2731

Font styles to use
Sans Serif

Requirements
Must have
• Company name, address, email and phone number.
• Also my name:
• Gustav R. Dresner
• Director
Nice to have
• Not a demand, but please consider creatively using the horizontal bar.
Should not have
• Cluttered of jumbled appearance.

```html
<!DOCTYPE html>
<html lang="en">
<head>
<meta charset="utf-8">
<title>Korvani Languages – Business Card</title>
<link rel="stylesheet" href="https://fonts.googleapis.com/css2?family=Open+Sans:wght@400;600;700&display=swap">
<style>
  :root {
    --backdrop: #2a2a2a;
    --card-white: #ffffff;
    --card-black: #1b1b1b;
    --ink-dark: #3f3f3f;
    --ink-mid: #555555;
    --accent: #f07a1a;
    --tab-grey: #4a4a4a;
  }
  * { box-sizing: border-box; margin: 0; padding: 0; }
  html, body {
    width: 1200px; height: 660px; overflow: hidden;
    background: var(--backdrop);
    font-family: "Open Sans", sans-serif;
  }
  .stage {
    position: relative; width: 1200px; height: 660px;
    display: flex; align-items: center; justify-content: center; gap: 40px;
  }
  .card {
    position: relative; width: 540px; height: 309px; overflow: hidden;
    box-shadow: 0 10px 30px rgba(0,0,0,.45);
  }
  .card--back {
    background: linear-gradient(160deg, #2a2a2a 0%, var(--card-black) 55%, #111 100%);
    display: flex; align-items: center; justify-content: center;
  }
  .card--front { background: var(--card-white); }

  .brand { display: flex; align-items: center; gap: 10px; }
  .brand__dot { width: 24px; height: 24px; border-radius: 50%; background: var(--accent); flex: none; }
  .brand__name {
    font-weight: 600; font-size: 15px; letter-spacing: 3px;
    text-transform: uppercase; line-height: 1;
  }
  .card--back .brand__name { color: #ffffff; }
  .card--front .brand { position: absolute; left: 30px; top: 128px; }
  .card--front .brand__name { color: var(--ink-mid); }

  .holder { position: absolute; right: 30px; top: 58px; text-align: right; }
  .holder__name { font-weight: 600; font-size: 22px; color: var(--ink-dark); line-height: 1.1; }
  .holder__title { font-weight: 600; font-size: 11px; color: var(--accent); }
  .rule-name {
    position: absolute; left: 210px; right: 30px; top: 102px;
    height: 2px; background: var(--ink-mid);
  }
  .rule-contact {
    position: absolute; left: 0; width: 270px; top: 192px;
    height: 1px; background: var(--ink-dark);
  }
  .contact { position: absolute; left: 30px; top: 200px; font-size: 11px; color: var(--ink-dark); line-height: 1.45; }
  .contact__row { display: flex; align-items: center; gap: 7px; }
  .contact__icon { width: 11px; height: 11px; flex: none; }
  .contact__company { margin-top: 4px; color: var(--accent); font-weight: 700; }
  .contact__address { font-weight: 600; }

  .band {
    position: absolute; left: 0; right: 0; bottom: 8px; height: 10px;
    background: var(--accent);
  }
  .band-tab {
    position: absolute; right: 0; bottom: 18px; width: 150px; height: 26px;
    background: var(--tab-grey); border-top-left-radius: 14px;
  }
</style>
</head>
<body>
<main class="stage">
  <section class="card card--back" aria-label="Card back">
    <div class="brand">
      <span class="brand__dot"></span>
      <span class="brand__name">Korvani Languages</span>
    </div>
  </section>

  <section class="card card--front" aria-label="Card front">
    <div class="holder">
      <p class="holder__name">Gustav R. Dresner</p>
      <p class="holder__title">Director</p>
    </div>
    <div class="rule-name"></div>

    <div class="brand">
      <span class="brand__dot"></span>
      <span class="brand__name">Korvani Languages</span>
    </div>

    <div class="rule-contact"></div>
    <div class="contact">
      <p class="contact__row">
        <svg class="contact__icon" viewBox="0 0 12 12" aria-hidden="true"><rect x="3" y="0.8" width="6" height="10.4" rx="1.2" fill="none" stroke="#f07a1a" stroke-width="1.4"/><circle cx="6" cy="9.2" r="0.7" fill="#f07a1a"/></svg>
        +1-888-604-2731
      </p>
      <p class="contact__row">
        <svg class="contact__icon" viewBox="0 0 12 12" aria-hidden="true"><rect x="0.5" y="2.2" width="11" height="7.6" fill="#f07a1a"/><path d="M0.8 2.6 L6 6.6 L11.2 2.6" fill="none" stroke="#fff" stroke-width="1"/></svg>
        gdresner@korvanilanguages.example
      </p>
      <p class="contact__company">Korvani Languages Worldwide, Ltd.</p>
      <p class="contact__address">#527-2368 Halden Crescent<br>Victoria, BC, Canada V9T3K2</p>
    </div>

    <div class="band-tab"></div>
    <div class="band"></div>
  </section>
</main>
</body>
</html>
```